Qorvant Flyer Design Project

We need a new flyer design for our company based in Australia. We provide Business Valuations for small businesses. The flyer should follow the same colours and theme as our website www.qorvant.com.au and our logo. The design should communicate a professional financial services company. It should be a simple design (not too 'busy') and have a sleek and professional feel to it. It will be used to send to prospective clients and referral sources to tell about our company and prompt them to call us or visit our website.

Target Market(s)

Business owners and people working in financial services (accountants, financial planners etc)

Industry/Entity Type

Financial

Requirements
Must have
• Must be DL double sided, (99mm x 210mm) and use CMYK colours. Must contain trim marks for printer and be print ready.

```html
<!DOCTYPE html>
<html lang="en">
<head>
<meta charset="utf-8">
<title>Qorvant DL Flyer</title>
<link href="https://fonts.googleapis.com/css2?family=Arimo:ital,wght@0,400;0,700;1,400;1,700&family=Open+Sans:ital,wght@0,400;0,700;1,700;1,800&family=PT+Sans:wght@400;700&display=swap" rel="stylesheet">
<style>
:root{
  --backdrop:#d8cdb0;
  --paper:#ffffff;
  --band:#eceee6;
  --brand-blue:#1a2fe0;
  --deep-blue:#0c1fd6;
  --card-blue-top:#5aa6f2;
  --card-blue-bottom:#1c49e6;
  --ink:#111111;
  --ink-soft:#3a3a3a;
  --accent-red:#e01010;
  --link-blue:#2f86e8;
  --frame:#8a8478;
  --panel-border:#d9ddd6;
  --tab-dark:#1a1a1a;
  --tick-green:#7cc242;
  --step-blue:#2f7fe0;
  --step-pink:#ee2a8a;
  --step-green:#3fcf3a;
  --bubble-grey:#d9d9d9;
}
*{box-sizing:border-box;margin:0;padding:0}
html,body{width:1200px;height:900px;overflow:hidden}
body{background:var(--backdrop);position:relative;font-family:"Arimo",Arial,sans-serif;color:var(--ink)}

.flyer{position:absolute;background:var(--paper);overflow:hidden}
.flyer--front{left:153px;top:28px;width:395px;height:838px}
.flyer--back{left:690px;top:40px;width:391px;height:826px}

.flyer__band{position:absolute;left:0;right:0;bottom:0;height:140px;background:var(--band)}
.flyer__frame{position:absolute;left:0;top:0}

.wordmark{position:absolute;font-family:"Arimo",Arial,sans-serif;font-weight:700;color:var(--brand-blue);font-size:30px;line-height:1;white-space:nowrap}
.tagline{position:absolute;font-family:"Arimo",Arial,sans-serif;font-style:italic;color:var(--brand-blue);line-height:1;white-space:nowrap}

/* front */
.headline{position:absolute;left:0;right:0;top:82px;text-align:center;font-style:italic;font-size:20px;line-height:29px}
.headline__accent{color:var(--accent-red)}

.step{position:absolute;border-radius:3px;color:#fff;font-family:"Open Sans",Arial,sans-serif;font-weight:700;font-style:italic;font-size:10.5px;line-height:14px;text-align:center;display:flex;align-items:center;justify-content:center;padding:8px 10px 0;box-shadow:0 4px 5px rgba(0,0,0,.18)}
.step__num{position:absolute;top:-14px;right:10px;width:26px;height:26px;border-radius:50%;font-size:19px;line-height:26px;font-family:"Arimo",serif;font-style:italic;font-weight:700;text-align:center}
.step--one{left:32px;top:317px;width:148px;height:62px;background:linear-gradient(#4d9af0,var(--step-blue))}
.step--one .step__num{background:var(--step-blue)}
.step--two{left:197px;top:331px;width:163px;height:66px;background:linear-gradient(#67e05e,var(--step-green))}
.step--two .step__num{background:var(--step-green)}
.step--three{left:143px;top:274px;width:141px;height:58px;background:linear-gradient(#f45aa5,var(--step-pink))}
.step--three .step__num{background:var(--step-pink)}

.figure{position:absolute;border-radius:12px}
.figure--presenter{left:255px;top:180px;width:92px;height:137px;background:linear-gradient(#e8e8e8,#2b2b2b)}
.figure--laptop{left:23px;top:532px;width:221px;height:130px;background:linear-gradient(#dfe3ea,#2a2a2a)}
.figure--cheer{left:245px;top:510px;width:118px;height:162px;background:linear-gradient(#ececec,#262626)}
.figure--runner{left:270px;top:590px;width:58px;height:60px;background:linear-gradient(#eeeeee,#333333)}

.callout{position:absolute;left:53px;top:430px;width:268px;height:66px;background:linear-gradient(#fafafa,var(--bubble-grey));border-radius:3px;box-shadow:0 3px 5px rgba(0,0,0,.2);font-family:"Open Sans",Arial,sans-serif;font-weight:800;font-style:italic;font-size:16px;line-height:21px;text-align:center;padding-top:12px;color:#1a1a1a}
.callout::after{content:"";position:absolute;right:38px;bottom:-12px;border-style:solid;border-width:12px 12px 0 0;border-color:var(--bubble-grey) transparent transparent transparent}

.seal{position:absolute;left:47px;bottom:68px;width:72px;height:72px;border-radius:50%;background:linear-gradient(135deg,#3ad0ff,var(--deep-blue))}
.seal-name{position:absolute;left:28px;bottom:30px;width:110px;text-align:center;font-family:"Arimo",Arial,sans-serif;font-weight:700;font-size:25px;color:var(--deep-blue)}
.strip{position:absolute;bottom:11px;height:17px;background:var(--deep-blue);color:#fff;font-size:12px;line-height:17px;text-align:center}
.strip--abn{left:17px;width:143px;font-style:italic}
.strip--mail{left:16px;width:142px;font-size:11px}

.office{position:absolute;bottom:12px;width:90px;height:114px;border-radius:4px;background:linear-gradient(var(--card-blue-top),var(--card-blue-bottom) 55%);padding:4px 5px;font-family:"PT Sans",Arial,sans-serif;color:#fff}
.office__title{font-size:10px;line-height:12px;padding-left:14px;position:relative;margin-bottom:5px}
.office__title::before{content:"";position:absolute;left:0;top:2px;width:8px;height:8px;border-radius:50%;background:#b9e04a}
.office__row{display:flex;gap:3px;align-items:flex-start;margin-bottom:4px}
.office__label{width:28px;text-align:right;font-size:5.5px;line-height:9px;color:#dfe8ff}
.office__value{flex:1;background:#fff;color:#222;font-size:5.5px;line-height:6.5px;border-radius:2px;padding:1.5px 3px}

/* back */
.intro{position:absolute;left:118px;top:74px;width:224px;height:68px;background:linear-gradient(#f6f6f6,#cfcfcf);box-shadow:0 3px 5px rgba(0,0,0,.2);font-family:"Open Sans",Arial,sans-serif;font-weight:700;font-style:italic;font-size:12.5px;line-height:16.5px;color:#555;text-align:center;padding-top:6px}
.intro::after{content:"";position:absolute;right:34px;bottom:-10px;border-style:solid;border-width:10px 0 0 10px;border-color:#cfcfcf transparent transparent transparent}

.reasons{position:absolute;left:38px;top:166px;width:310px;height:502px;border:7px solid var(--panel-border);border-radius:22px;background:linear-gradient(#fff,#f1f3ef)}
.reasons__tab{position:absolute;left:44px;top:-15px;width:214px;height:54px;background:linear-gradient(#444,var(--tab-dark));border-radius:0 0 14px 14px;color:#fff;font-family:"PT Sans",Arial,sans-serif;font-size:21px;line-height:58px;text-align:center}
.reasons__list{list-style:none;position:absolute;left:17px;top:62px;width:262px;font-family:"PT Sans",Arial,sans-serif;font-size:12.6px;line-height:13.5px;color:var(--ink-soft)}
.reasons__item{position:relative;padding-left:24px;margin-bottom:14px}
.reasons__item::before{content:"";position:absolute;left:0;top:0;width:14px;height:14px;border-radius:50%;background:radial-gradient(#fff,#dfe6da)}
.reasons__item::after{content:"";position:absolute;left:4px;top:2px;width:5px;height:8px;border:solid var(--tick-green);border-width:0 2.5px 2.5px 0;transform:rotate(40deg)}
.reasons__item--hi{color:var(--link-blue)}
.reasons__hi{color:var(--link-blue)}
.reasons__rule{position:absolute;left:18px;right:18px;top:410px;border-top:1px solid #ddd}
.reasons__contact{position:absolute;left:0;width:232px;top:416px;text-align:center;font-family:"PT Sans",Arial,sans-serif;font-size:13px;line-height:16px;color:var(--ink)}
.reasons__phone{color:var(--accent-red);font-weight:700;font-style:italic}
.url-button{position:absolute;left:73px;top:451px;width:152px;height:30px;border-radius:4px;background:linear-gradient(#fafafa,#cfcfcf);box-shadow:0 2px 3px rgba(0,0,0,.25);font-family:"PT Sans",Arial,sans-serif;font-weight:700;font-size:12px;line-height:30px;color:#333;padding-left:10px}
.url-button__go{position:absolute;right:2px;top:2px;width:24px;height:26px;background:#111;border-radius:3px}
.url-button__go svg{display:block;margin:6px auto}
.reasons .figure--runner{left:225px;top:424px}
</style>
</head>
<body>

<!-- FRONT -->
<section class="flyer flyer--front">
  <div class="flyer__band"></div>
  <svg class="flyer__frame" width="395" height="838" viewBox="0 0 395 838">
    <path d="M14 680 V30 Q14 16 28 16 H140 Q150 16 155 28 L162 46 Q168 60 182 60 H370 Q381 60 381 72 V680 Q381 694 367 694 H28 Q14 694 14 680 Z" fill="#fff" stroke="var(--frame)" stroke-width="1.5"/>
  </svg>
  <div class="wordmark" style="left:22px;top:31px">Qorvant</div>
  <div class="tagline" style="left:176px;top:30px;font-size:20px">Business Valuations</div>

  <p class="headline">Before you buy or sell a business<br>let us check the numbers<br><span class="headline__accent">for just 3 simple steps</span></p>

  <div class="figure figure--presenter" role="img" aria-label="3D character in a suit presenting the steps"></div>
  <div class="step step--three"><span class="step__num">3</span>Your valuation Report<br>is emailed to you</div>
  <div class="step step--one"><span class="step__num">1</span>Provide information<br>about the business</div>
  <div class="step step--two"><span class="step__num">2</span>A qualified Accountant<br>analyses the business</div>

  <div class="callout">We conduct business valuations<br>of Australian small businesses</div>

  <div class="figure figure--laptop" role="img" aria-label="Laptop showing a business valuation report, with a mouse"></div>
  <div class="figure figure--cheer" role="img" aria-label="3D character in a suit cheering with raised arms"></div>

  <div class="seal"></div>
  <div class="seal-name">qorvant</div>
  <div class="strip strip--abn">ABN 51 304 882 716</div>

  <div class="office" style="left:180px">
    <div class="office__title">Queensland</div>
    <div class="office__row"><span class="office__label">Address</span><span class="office__value">PO Box 514<br>Coral Cove<br>Queensland</span></div>
    <div class="office__row"><span class="office__label">Post Code</span><span class="office__value">4286</span></div>
    <div class="office__row"><span class="office__label">Phone</span><span class="office__value">1300 482 615</span></div>
    <div class="office__row"><span class="office__label">Fax</span><span class="office__value">(07) 5610 2847</span></div>
  </div>
  <div class="office" style="left:285px">
    <div class="office__title">Victoria</div>
    <div class="office__row"><span class="office__label">Address</span><span class="office__value">PO Box 18742<br>Harbourside<br>Victoria</span></div>
    <div class="office__row"><span class="office__label">Post Code</span><span class="office__value">8047</span></div>
    <div class="office__row"><span class="office__label">Phone</span><span class="office__value">1300 482 615</span></div>
    <div class="office__row"><span class="office__label">Fax</span><span class="office__value">(03) 8610 4495</span></div>
  </div>
</section>

<!-- BACK -->
<section class="flyer flyer--back">
  <div class="flyer__band"></div>
  <svg class="flyer__frame" width="391" height="826" viewBox="0 0 391 826">
    <path d="M16 668 V26 Q16 12 30 12 H146 Q156 12 161 24 L168 42 Q174 56 188 56 H366 Q376 56 376 68 V668 Q376 682 362 682 H30 Q16 682 16 668 Z" fill="#fff" stroke="var(--frame)" stroke-width="1.5"/>
  </svg>
  <div class="wordmark" style="left:25px;top:25px">Qorvant</div>
  <div class="tagline" style="left:180px;top:30px;font-size:13px">small business valuation experts</div>

  <div class="intro">Qorvant is an Accounting service<br>that specialises in preparing small<br>business valuation reports.</div>

  <div class="reasons">
    <div class="reasons__tab">Why use Qorvant ?</div>
    <ul class="reasons__list">
      <li class="reasons__item reasons__item--hi">Qualified Accountant spends time review-<br>ing every business.</li>
      <li class="reasons__item"><span class="reasons__hi">Specialised</span> – valuing small businesses is all we do.</li>
      <li class="reasons__item">We use our experience to compare and benchmark similar businesses across Australia.</li>
      <li class="reasons__item">A valuation appraisal report emailed to you with our comments and valuation estimate.</li>
      <li class="reasons__item reasons__item--hi">Five business day turnaround!</li>
      <li class="reasons__item">A follow up phone call from an Accoun-<br>tant to discuss the valuation and answer any questions you have.</li>
      <li class="reasons__item reasons__item--hi">Fixed price of only $540 (+gst).</li>
      <li class="reasons__item">Our clients include Business Buyers and Sellers, Accountants, Solicitors, Financial Planners, Franchisors and Franchisees.</li>
    </ul>
    <div class="reasons__rule"></div>
    <p class="reasons__contact">For more info call <span class="reasons__phone">1300 482 615</span><br>or visit</p>
    <div class="url-button">www.qorvant.com.au
      <span class="url-button__go"><svg width="12" height="14" viewBox="0 0 12 14"><path d="M1 1 L11 7 L1 13 Z" fill="#fff"/></svg></span>
    </div>
    <div class="figure figure--runner" role="img" aria-label="Small 3D character in a suit running"></div>
  </div>

  <div class="seal"></div>
  <div class="seal-name">qorvant</div>
  <div class="strip strip--mail">info@qorvant.com.au</div>

  <div class="office" style="left:177px">
    <div class="office__title">Queensland</div>
    <div class="office__row"><span class="office__label">Address</span><span class="office__value">PO Box 514<br>Coral Cove<br>Queensland</span></div>
    <div class="office__row"><span class="office__label">Post Code</span><span class="office__value">4286</span></div>
    <div class="office__row"><span class="office__label">Phone</span><span class="office__value">1300 482 615</span></div>
    <div class="office__row"><span class="office__label">Fax</span><span class="office__value">(07) 5610 2847</span></div>
  </div>
  <div class="office" style="left:280px">
    <div class="office__title">Victoria</div>
    <div class="office__row"><span class="office__label">Address</span><span class="office__value">PO Box 18742<br>Harbourside<br>Victoria</span></div>
    <div class="office__row"><span class="office__label">Post Code</span><span class="office__value">8047</span></div>
    <div class="office__row"><span class="office__label">Phone</span><span class="office__value">1300 482 615</span></div>
    <div class="office__row"><span class="office__label">Fax</span><span class="office__value">(03) 8610 4495</span></div>
  </div>
</section>

</body>
</html>
```